Guarding One's Body Using Sharp Steel Cover

Hi we are producing a self defense course entitled Guarding One's Body Using Sharp Steel: A Complete Manual For Learning The Finest And Handiest Wilderness Tool In Recorded History.

I listed this as a book cover but it will actually be a DVD set, but the book cover model works fine.

See below for design examples - I am thinking we need a cover that will appeal to military/survival type people.

Target Market(s)

survivalists, cops, preppers, gun owners, martial artists, and average people wanting to learn how to defend themselves

Industry/Entity Type

Defense

Requirements
Must have
• Title: GUARDING ONE'S BODY USING SHARP STEEL: A COMPLETE MANUAL FOR LEARNING THE FINEST AND HANDIEST WILDERNESS TOOL IN RECORDED HISTORY
Nice to have
• Please look at these sample designs from other books as a model:
• https://files.plorvexa.org/media/en/4/27/BrindelQXMP.jpg - This stye is ideal.
• Other good examples:
• https://pics2.talvorn.com/8143907_k370.jpg
• http://m.zephquill.com/titles/2719058463k/48071935.jpg
• http://img.crondelmart.com/pics/P/73Tm58QyzFr._BX_KL410_TR316,410_.jpg
• http://3.cdn.wendoplix.net/-RTyZWLMMKAQ/BNWq_hufxaT/BBBBBBBBv8G/DKNp815ZaXW/s1600/Q4710392.JPG

```html
<!DOCTYPE html>
<html lang="en">
<head>
<meta charset="utf-8">
<title>Guarding One's Body Using Sharp Steel – Cover Spread</title>
<link rel="stylesheet" href="https://fonts.googleapis.com/css2?family=Jost:wght@300;400;500&family=Black+Ops+One&family=Oswald:wght@500&display=swap">
<style>
  :root {
    --page: #ffffff;
    --camo-light: #a9b486;
    --camo-mid: #8e9c6c;
    --camo-dark: #6f7f56;
    --panel: rgba(63, 92, 78, 0.72);
    --copy-box: #dfe5e1;
    --spine: #24474a;
    --white: #ffffff;
    --front-top: #b9bcb4;
    --front-glow: #ecebc6;
    --title-green: #355e34;
    --title-edge: #1f3a22;
    --sub-maroon: #6a1f2c;
    --knife-dark: #203f44;
    --knife-mid: #3f6f73;
    --publisher: #2c4a2d;
  }
  * { margin: 0; padding: 0; box-sizing: border-box; }
  html, body { width: 852px; height: 1200px; overflow: hidden; background: var(--page); }
  .canvas { position: relative; width: 852px; height: 1200px; }

  .spread {
    position: absolute; left: 88px; top: 107px;
    width: 681px; height: 450px; display: flex;
  }

  /* Back cover */
  .back-cover {
    position: relative; width: 320px; height: 100%;
    background:
      radial-gradient(ellipse 60% 40% at 30% 20%, var(--camo-light), transparent 70%),
      radial-gradient(ellipse 50% 35% at 75% 70%, var(--camo-light), transparent 70%),
      radial-gradient(ellipse 45% 30% at 20% 80%, var(--camo-dark), transparent 70%),
      var(--camo-mid);
  }
  .back-title {
    position: absolute; top: 32px; left: 0; width: 100%;
    text-align: center; color: var(--white);
    font: 400 12px/1.2 "Jost", sans-serif; text-transform: uppercase;
  }
  .back-panel {
    position: absolute; left: 44px; top: 74px; width: 226px; height: 301px;
    background: var(--panel);
  }
  .back-tagline {
    position: absolute; top: 14px; left: 0; width: 100%;
    text-align: center; color: var(--white);
    font: 300 10px/1.3 "Jost", sans-serif;
  }
  .back-copy-box {
    position: absolute; left: 15px; top: 67px; width: 195px; height: 202px;
    background: var(--copy-box);
  }

  /* Spine */
  .spine {
    position: relative; width: 37px; height: 100%; background: var(--spine);
  }
  .spine-title {
    position: absolute; top: 36px; left: 50%;
    transform-origin: 0 0; transform: rotate(90deg) translateY(-50%);
    white-space: nowrap; color: var(--white);
    font: 400 14px/1 "Jost", sans-serif; text-transform: uppercase;
  }

  /* Front cover */
  .front-cover {
    position: relative; flex: 1; height: 100%; overflow: hidden;
    background: radial-gradient(ellipse 80% 70% at 55% 95%, var(--front-glow), var(--front-top) 85%);
  }
  .front-title {
    position: absolute; top: 16px; left: 0; width: 100%;
    text-align: center; color: var(--title-green);
    font: 400 30px/1.15 "Black Ops One", sans-serif; text-transform: uppercase;
    -webkit-text-stroke: 1px var(--title-edge);
  }
  .front-subtitle {
    position: absolute; top: 150px; left: 0; width: 100%;
    text-align: center; color: var(--sub-maroon);
    font: 500 12.5px/1.5 "Oswald", sans-serif; text-transform: uppercase;
    -webkit-text-stroke: 0.4px var(--white);
    text-shadow: 0 0 2px var(--white), 0 0 2px var(--white);
  }
  .knife-art {
    position: absolute; left: 22px; top: 375px; width: 330px; height: 40px;
    border-radius: 6px 20px 20px 6px;
    background: linear-gradient(180deg, var(--knife-mid), var(--knife-dark));
    transform-origin: 0 50%; transform: rotate(-31deg);
  }
  .publisher {
    position: absolute; bottom: 18px; left: 0; width: 100%;
    text-align: center; color: var(--publisher);
    font: 500 19px/1 "Jost", sans-serif; letter-spacing: 1px; text-transform: uppercase;
  }
</style>
</head>
<body>
<div class="canvas">
  <div class="spread">
    <section class="back-cover" role="img" aria-label="Back cover with green camouflage background">
      <p class="back-title">Guarding One's Body Using Sharp Steel</p>
      <div class="back-panel">
        <p class="back-tagline">A Complete Manual For Learning<br>The Finest And Handiest Wilderness<br>Tool In Recorded History</p>
        <div class="back-copy-box"></div>
      </div>
    </section>

    <section class="spine">
      <p class="spine-title">Guarding One's Body Using Sharp Steel</p>
    </section>

    <section class="front-cover">
      <div class="knife-art" role="img" aria-label="Illustration of a dark teal combat knife pointing diagonally down to the left"></div>
      <h1 class="front-title">Guarding One's<br>Body Using<br>Sharp Steel:</h1>
      <p class="front-subtitle">A Complete Manual For Learning<br>The Finest And Handiest<br>Wilderness Tool In Recorded History</p>
      <p class="publisher">Steadfast Edge Video</p>
    </section>
  </div>
</div>
</body>
</html>
```